Banner ad to encourage people to complete a survey

This is a banner ad which will be posted on www.veltrona.org. The goal of the add is to encourage people to click on it and take the survey.
File Format: Standard .jpg image (no Flash)
Ad dimension (Pixels): 300w x 250d
Max File Size: 24k
- Use a border to differentiate the banner from page content (page background is white)
- No transparent backgrounds
Ad Message: "Speech-Language Pathologist Survey"
Additional text: "Please take two minutes to complete a survey on the future of work patterns for Speech-Language Pathologists and enter a draw to win an Zorbik"
Target Market(s)
The respondents are professional and well educated and the ad/colour scheme should reflect this.
Font styles to use
Colors
Designer to choose colors to be used in the design.
Look and feel

```html
<!DOCTYPE html>
<html lang="en">
<head>
<meta charset="utf-8">
<title>Speech-Language Pathologist Survey – Banner</title>
<link rel="stylesheet" href="https://fonts.googleapis.com/css2?family=Raleway:wght@600&family=Open+Sans:wght@400;600;700&display=swap">
<style>
  :root {
    --page-bg: #ebe8e4;
    --banner-purple: #7d5389;
    --title-bg: #ffffff;
    --title-ink: #1f3656;
    --stripe-blue: #2f5ea8;
    --stripe-red: #c8283f;
    --body-ink: #ffffff;
    --button-bg: #25344a;
    --button-ink: #ffffff;
    --accent-pink: #e6a0d8;
    --art-light: #a57fb0;
    --art-dark: #5e3c6a;
  }
  * { margin: 0; padding: 0; box-sizing: border-box; }
  html, body {
    width: 1200px;
    height: 710px;
    overflow: hidden;
    background: var(--page-bg);
  }
  .banner {
    position: absolute;
    left: 228px;
    top: 45px;
    width: 744px;
    height: 620px;
    background: var(--banner-purple);
    overflow: hidden;
  }
  .title-block {
    position: absolute;
    left: 0;
    top: 20px;
    width: 650px;
    height: 149px;
    background: var(--title-bg);
    padding: 12px 0 0 30px;
  }
  .title-block h1 {
    font-family: "Raleway", sans-serif;
    font-weight: 600;
    font-size: 46px;
    line-height: 62px;
    color: var(--title-ink);
  }
  .stripe {
    position: absolute;
    top: 20px;
    height: 149px;
  }
  .stripe--blue { left: 650px; width: 18px; background: var(--stripe-blue); }
  .stripe--red  { left: 670px; width: 12px; background: var(--stripe-red); }
  .intro {
    position: absolute;
    left: 30px;
    top: 210px;
    width: 660px;
    font-family: "Open Sans", sans-serif;
    font-weight: 400;
    font-size: 34px;
    line-height: 45px;
    color: var(--body-ink);
  }
  .survey-art {
    position: absolute;
    left: 360px;
    top: 320px;
    width: 384px;
    height: 300px;
    background: linear-gradient(160deg, var(--art-light), var(--art-dark));
    border-top-left-radius: 40px;
  }
  .cta {
    position: absolute;
    left: 25px;
    top: 476px;
    width: 292px;
    height: 119px;
    border-radius: 12px;
    background: var(--button-bg);
    color: var(--button-ink);
    font-family: "Open Sans", sans-serif;
    font-weight: 600;
    font-size: 26px;
    line-height: 36px;
    letter-spacing: 0.5px;
    padding: 22px 0 0 20px;
    text-transform: uppercase;
  }
  .cta__prize { color: var(--accent-pink); font-weight: 700; }
</style>
</head>
<body>
  <main class="banner">
    <div class="title-block">
      <h1>Speech-Language<br>Pathologist Survey</h1>
    </div>
    <div class="stripe stripe--blue"></div>
    <div class="stripe stripe--red"></div>

    <p class="intro">Please take two minutes to complete<br>a survey on the future of work<br>patterns for<br>Speech-Language<br>Pathologists</p>

    <div class="survey-art" role="img" aria-label="Illustration of hands holding a tablet showing a survey form with checkboxes"></div>

    <div class="cta">Enter a draw<br>to win an <span class="cta__prize">Zorbik</span></div>
  </main>
</body>
</html>
```